Website for Public Relations Agency called "Bright Lark"

A need a website for a new business which is essentially a Public Relations/ Marketing business. We offer services to small family businesses, medium enterprise as well as multinational companies (ie we sell our professional services to other businesses; we are not a consumer brand).
The website needs to be polished, professional and modern. Because of the services we offer, I really need the website to be a little bit "wow".
Colours - we have a logo (see files) so the colour palette for the website should be dictated by this.
The Word doc attached mapped out the various pages that will make up the site. The text is not 100% finalised but it's good enough to give you a good picture of what the site will talk about.
I am not selling directly off my site, so this is an informational site only to explain who i am and what i do.
Target Market(s)
Other businesses - small family business, medium business and large multinational companies
Industry/Entity Type
Marketing
Coding
Coded - Design and coding required
Number of Pages Required
5+ page
Requirements
Must have
- Given my business, really looking for a little "wow" factor on the home page
Should not have
- I don't know if this is relevant to the coding, but I want to end up on a platform that I can myself make copy/ text edits as I please. I do not want to have to go through a deisgn company for small text changes in 6 or 12 months time.

```html
<!DOCTYPE html>
<html lang="en">
<head>
<meta charset="UTF-8">
<title>Bright Lark – Strategic Communication</title>
<link href="https://fonts.googleapis.com/css2?family=Lato:wght@400;700&display=swap" rel="stylesheet">
<style>
:root{
  --pink:#d94f9b;
  --purple:#967db0;
  --sky:#8fd8f0;
  --ink:#444444;
  --text:#3a3a3a;
  --white:#ffffff;
  --rule:#e4e4e4;
}
*{box-sizing:border-box;margin:0;padding:0}
html,body{width:1200px;height:2937px;overflow:hidden;background:var(--white)}
body{font-family:'Lato',sans-serif;color:var(--text);position:relative}
.abs{position:absolute}

/* header */
.site-header{position:absolute;left:0;top:0;width:1200px;height:103px}
.brand{position:absolute;left:112px;top:26px;display:flex;align-items:center;gap:12px}
.brand-dot{width:22px;height:22px;border-radius:50%;background:var(--pink)}
.brand-name{font-size:36px;font-weight:700;color:var(--pink);line-height:1}
.main-nav a{position:absolute;top:40px;font-size:15px;color:var(--ink);text-decoration:none}
.main-nav .is-active{left:502px;top:31px;width:73px;height:38px;background:var(--pink);color:var(--white);font-weight:700;border-radius:3px;text-align:center;line-height:38px;font-size:16px}

/* hero */
.hero{position:absolute;left:0;top:103px;width:1200px;height:600px;background:var(--sky);overflow:hidden}
.hero-visual{position:absolute;left:540px;top:0;width:660px;height:600px;background:linear-gradient(110deg,var(--sky) 0%,#5fb4dc 45%,#24466f 100%)}
.hero-title{position:absolute;left:112px;top:152px;font-size:57px;font-weight:700;line-height:61px;color:var(--pink)}
.hero-sub{position:absolute;left:112px;top:297px;font-size:27px;font-weight:700;line-height:35px;color:var(--ink);width:520px}
.hero-copy{position:absolute;left:112px;top:385px;font-size:20px;line-height:26.5px;color:var(--ink);width:470px}

/* intro */
.intro-photo{left:112px;top:790px;width:458px;height:603px;border-radius:8px;background:linear-gradient(160deg,#c9d6e2,#7d8fa3 55%,#2e3a52)}
.section-title{font-size:43px;font-weight:700;line-height:48px}
.section-title .pink{color:var(--pink)}
.section-title .purple{color:var(--purple)}
.intro-title{left:643px;top:783px;width:460px}
.question-list{left:643px;top:905px;width:450px;list-style:none}
.question-list li{position:relative;padding-left:52px;font-size:16.5px;line-height:24px;margin-bottom:14px}
.question-list li::before{content:"";position:absolute;left:4px;top:6px;width:22px;height:22px;border:2.5px solid var(--pink);border-radius:50%}
.intro-close{left:645px;top:1322px;width:450px;font-size:16.5px;line-height:24px}

/* services */
.services-title{left:0;top:1470px;width:1200px;text-align:center}
.carousel-arrow{width:27px;height:27px;border-radius:50%;background:var(--pink);top:1661px}
.service{text-align:center;font-size:27px;line-height:31px;color:var(--ink)}
.service-card{left:458px;top:1602px;width:320px;height:197px;background:var(--purple);border-radius:3px;color:var(--white);font-weight:700;font-size:24px;line-height:31px;display:flex;align-items:center;justify-content:center;padding:0 16px;text-align:center}

/* clients */
.clients{left:28px;top:1885px;width:1144px;height:422px;background:var(--pink);border-radius:12px;color:var(--white);text-align:center}
.clients h2{margin-top:72px;font-size:44px;font-weight:700}
.clients blockquote{width:840px;margin:16px auto 0;font-size:20.5px;line-height:26px}
.clients .client-name{margin-top:20px;font-weight:700;font-size:20px}
.clients .client-org{margin-top:10px;font-size:20px}
.dots{display:flex;gap:8px;justify-content:center;margin-top:16px}
.dots span{width:17px;height:5px;background:var(--white)}

/* footer */
.footer-brand{left:0;top:2420px;width:1200px;display:flex;justify-content:center;align-items:center;gap:22px}
.footer-brand .brand-dot{width:44px;height:44px}
.footer-brand .brand-name{font-size:80px}
.acknowledgement{left:215px;top:2594px;width:770px;text-align:center;font-size:16.5px;line-height:24px}
.footer-nav{left:0;top:2722px;width:1200px;display:flex;justify-content:center;gap:32px;font-size:17px}
.footer-nav a{color:var(--ink);text-decoration:none}
.footer-nav .sep{color:var(--ink)}
.footer-nav .social{color:var(--pink)}
.contact{display:flex;align-items:center;gap:20px;top:2780px}
.contact-icon{width:60px;height:60px;border-radius:50%;background:var(--purple);display:flex;align-items:center;justify-content:center}
.contact-label{color:var(--purple);font-weight:700;font-size:17px}
.contact-value{font-size:17px;margin-top:4px}
.footer-rule{left:112px;top:2896px;width:976px;height:1px;background:var(--rule)}
.copyright{left:0;top:2911px;width:1200px;text-align:center;font-size:13px;color:var(--ink)}
</style>
</head>
<body>

<header class="site-header">
  <div class="brand"><span class="brand-dot"></span><span class="brand-name">Bright Lark</span></div>
  <nav class="main-nav">
    <a class="is-active" href="#">Home</a>
    <a href="#" style="left:630px">About</a>
    <a href="#" style="left:742px">How We Help</a>
    <a href="#" style="left:905px">Fees</a>
    <a href="#" style="left:1005px">Get In Touch</a>
  </nav>
</header>

<section class="hero">
  <div class="hero-visual" role="img" aria-label="Hand touching a tablet with glowing business growth charts rising above it"></div>
  <h1 class="hero-title">Carefully Considered.<br>Expertly Crafted.</h1>
  <p class="hero-sub">Strategic Communication &amp; Reputation Management Specialist</p>
  <p class="hero-copy">When you have a message to deliver, a story to tell, something to say that you need your stakeholders to hear loud and clear… Bright Lark can help.</p>
</section>

<div class="abs intro-photo" role="img" aria-label="Businesswoman presenting documents to colleagues around a meeting table"></div>
<h2 class="abs section-title intro-title"><span class="pink">In Business, Messaging</span><br><span class="purple">Always Matters</span></h2>
<ul class="abs question-list">
  <li>Do you have a message to share that will build trust with the audiences that drive your revenue?</li>
  <li>Perhaps you need help promoting your people or services, or ensure they are known by a wider audience?</li>
  <li>Is there a narrative to be carefully devised and managed to prevent the erosion of trust amongst your important stakeholders, either internal or external?</li>
  <li>Do you have a situation on your hands, and you feel like you need to go into damage control?</li>
  <li>Has the media come knocking and you’re not sure what to say?</li>
  <li>Do you need a website that is cohesive and sharp?</li>
</ul>
<p class="abs intro-close">Get in touch. We’d love to talk about how we can help shape your narrative, overcome your communications challenges, and support you to say what needs to be said.</p>

<h2 class="abs section-title services-title"><span class="pink">We Help You Communicate With</span><br><span class="purple">Clarity &amp; Impact</span></h2>
<div class="abs carousel-arrow" style="left:42px"><svg width="27" height="27" viewBox="0 0 27 27"><path d="M15.5 8 L10 13.5 L15.5 19" stroke="#fff" stroke-width="2.5" fill="none" stroke-linecap="round"/></svg></div>
<div class="abs carousel-arrow" style="left:1131px"><svg width="27" height="27" viewBox="0 0 27 27"><path d="M11.5 8 L17 13.5 L11.5 19" stroke="#fff" stroke-width="2.5" fill="none" stroke-linecap="round"/></svg></div>
<p class="abs service" style="left:100px;top:1656px;width:280px">Media strategy, liaison, management and execution</p>
<div class="abs service-card">Crisis, Issues &amp; Reputation Management (specialising in post cyber incident communications)</div>
<p class="abs service" style="left:845px;top:1656px;width:260px">Executive &amp; Internal Communication</p>

<section class="abs clients">
  <h2>Our Clients</h2>
  <blockquote>“We engaged Clara Weston of Bright Lark to assist with an announcement about leadership changes and growth ambitions. Crafting the right message for our market was a challenge; strategically we were hoping for some industry media coverage. Clara did what Clara said she would and successfully secured this coverage to meet our objectives.&nbsp; ...</blockquote>
  <p class="client-name">Marcus Hale</p>
  <p class="client-org">Harbour Underwriting</p>
  <div class="dots"><span></span><span></span><span></span></div>
</section>

<footer>
  <div class="abs footer-brand"><span class="brand-dot"></span><span class="brand-name">Bright Lark</span></div>
  <p class="abs acknowledgement">Bright Lark acknowledges the Traditional Owners of Country throughout the land we call Australia. In particular, we pay our respect to the Cammeraygal people of the Eora nation whose Country our business operates from. Indeed, we recognise all First Nations peoples’ continuing connection to land, waters and culture and pay our respects to their Elders past and present.</p>
  <nav class="abs footer-nav">
    <a href="#">Home</a><span class="sep">|</span>
    <a href="#">About</a><span class="sep">|</span>
    <a href="#">How We Help</a><span class="sep">|</span>
    <a href="#">Fees</a><span class="sep">|</span>
    <a href="#">Get In Touch</a><span class="sep">|</span>
    <a class="social" href="#">Network</a>
  </nav>
  <div class="abs contact" style="left:316px">
    <div class="contact-icon"><svg width="32" height="22" viewBox="0 0 32 22"><rect x="1" y="1" width="30" height="20" rx="2" fill="none" stroke="#fff" stroke-width="2"/><path d="M1 2 L16 13 L31 2" fill="none" stroke="#fff" stroke-width="2"/></svg></div>
    <div><p class="contact-label">Email</p><p class="contact-value">clara.weston@brightlark.com.au</p></div>
  </div>
  <div class="abs contact" style="left:676px">
    <div class="contact-icon"><svg width="28" height="28" viewBox="0 0 24 24"><path d="M6.6 10.8a15 15 0 0 0 6.6 6.6l2.2-2.2a1 1 0 0 1 1-.25 11.4 11.4 0 0 0 3.6.57 1 1 0 0 1 1 1V20a1 1 0 0 1-1 1A17 17 0 0 1 3 4a1 1 0 0 1 1-1h3.5a1 1 0 0 1 1 1c0 1.25.2 2.45.57 3.57a1 1 0 0 1-.25 1z" fill="#fff"/></svg></div>
    <div><p class="contact-label">Phone</p><p class="contact-value">+61 412 555 018</p></div>
  </div>
  <div class="abs footer-rule"></div>
  <p class="abs copyright">Copyright © 2024&nbsp; Bright Lark. All rights reserved.</p>
</footer>

</body>
</html>
```